Inforgraphics Design for American English Vs British English Feb 2019

Create a Corporate looking design.

It is for infographics of Amercian English Vs British English.

It is for posting in Pingvale.

```html
<!DOCTYPE html>
<html lang="en">
<head>
<meta charset="utf-8">
<title>American English vs British English</title>
<link rel="stylesheet" href="https://fonts.googleapis.com/css2?family=Montserrat:wght@800&family=Patrick+Hand&family=Libre+Baskerville:wght@700&display=swap">
<style>
  :root {
    --title-red: #e0373d;
    --vs-blue: #1f6fc2;
    --white: #ffffff;
    --chip-light: #f4e9c9;
    --chip-mid: #e6d3a2;
    --chip-deep: #d9c189;
    --board: #2a2a2a;
    --frame: #a87549;
    --chalk: #f6f6f2;
    --flag-red: #c8102e;
    --flag-blue: #012169;
    --us-blue: #3c3b6e;
    --us-red: #b22234;
    --brand: #c9362c;
  }
  * { margin: 0; padding: 0; box-sizing: border-box; }
  html, body { width: 1200px; height: 1200px; overflow: hidden; background: var(--white); }
  .canvas { position: relative; width: 1200px; height: 1200px; overflow: hidden; }
  .backdrop {
    position: absolute; left: 0; top: 0; width: 1200px; height: 1080px;
    background:
      radial-gradient(ellipse at 25% 30%, var(--chip-light) 0%, transparent 55%),
      radial-gradient(ellipse at 75% 70%, var(--chip-light) 0%, transparent 55%),
      linear-gradient(135deg, var(--chip-mid), var(--chip-deep) 50%, var(--chip-mid));
  }
  .divider { position: absolute; left: 0; top: 0; width: 1200px; height: 1080px; }
  .title {
    position: absolute; top: 190px; width: 640px; text-align: center;
    font-family: "Montserrat", sans-serif; font-weight: 800; font-size: 92px; line-height: 128px;
    color: var(--title-red); letter-spacing: -1px;
    -webkit-text-stroke: 5px var(--white); paint-order: stroke fill;
    text-shadow: 0 3px 6px rgba(120, 80, 20, 0.25);
  }
  .title--us { left: -13px; }
  .title--uk { left: 600px; }
  .vs-badge {
    position: absolute; left: 538px; top: 404px; width: 138px; height: 138px; border-radius: 50%;
    background: var(--white); display: flex; align-items: center; justify-content: center;
    font-family: "Montserrat", sans-serif; font-weight: 800; font-size: 60px; color: var(--vs-blue);
    box-shadow: 0 3px 10px rgba(0,0,0,0.15);
  }
  .flag { position: absolute; top: 473px; width: 353px; height: 190px; }
  .flag--us { left: 120px; }
  .flag--uk { left: 747px; }
  .chalkboard {
    position: absolute; top: 773px; width: 309px; height: 214px;
    background: var(--board); border: 9px solid var(--frame);
    box-shadow: 0 4px 10px rgba(0,0,0,0.3);
    display: flex; align-items: center; justify-content: center; text-align: center;
    font-family: "Patrick Hand", cursive; color: var(--chalk); font-size: 60px; line-height: 58px;
  }
  .chalkboard--us { left: 144px; }
  .chalkboard--uk { left: 767px; }
  .footer {
    position: absolute; left: 0; top: 1080px; width: 1200px; height: 120px; background: var(--white);
    display: flex; align-items: center; justify-content: center; gap: 14px;
  }
  .brand-dot { width: 34px; height: 34px; border-radius: 50%; background: var(--brand); }
  .brand-name { font-family: "Libre Baskerville", serif; font-weight: 700; font-size: 34px; color: var(--brand); }
</style>
</head>
<body>
<main class="canvas">
  <div class="backdrop" role="img" aria-label="Close-up photo of a pile of golden potato crisps"></div>

  <svg class="divider" viewBox="0 0 1200 1080" aria-hidden="true">
    <line x1="667" y1="0" x2="520" y2="1080" stroke="#ffffff" stroke-width="7"/>
  </svg>

  <h1 class="title title--us">Amercian<br>English</h1>
  <h2 class="title title--uk">British<br>English</h2>

  <div class="vs-badge">vs</div>

  <svg class="flag flag--us" viewBox="0 0 247 130" preserveAspectRatio="none" role="img" aria-label="Flag of the United States">
    <defs>
      <pattern id="stars" width="16.5" height="14" patternUnits="userSpaceOnUse">
        <circle cx="8" cy="7" r="2.6" fill="#ffffff"/>
      </pattern>
    </defs>
    <rect width="247" height="130" fill="#ffffff"/>
    <g fill="#b22234">
      <rect y="0" width="247" height="10"/><rect y="20" width="247" height="10"/>
      <rect y="40" width="247" height="10"/><rect y="60" width="247" height="10"/>
      <rect y="80" width="247" height="10"/><rect y="100" width="247" height="10"/>
      <rect y="120" width="247" height="10"/>
    </g>
    <rect width="99" height="70" fill="#3c3b6e"/>
    <rect width="99" height="70" fill="url(#stars)"/>
  </svg>

  <svg class="flag flag--uk" viewBox="0 0 60 30" preserveAspectRatio="none" role="img" aria-label="Flag of the United Kingdom">
    <rect width="60" height="30" fill="#012169"/>
    <path d="M0,0 L60,30 M60,0 L0,30" stroke="#ffffff" stroke-width="6"/>
    <path d="M0,0 L60,30 M60,0 L0,30" stroke="#c8102e" stroke-width="2"/>
    <path d="M30,0 V30 M0,15 H60" stroke="#ffffff" stroke-width="10"/>
    <path d="M30,0 V30 M0,15 H60" stroke="#c8102e" stroke-width="6"/>
  </svg>

  <div class="chalkboard chalkboard--us">Chips</div>
  <div class="chalkboard chalkboard--uk">french<br>fries</div>

  <footer class="footer">
    <span class="brand-dot"></span>
    <span class="brand-name">Lexbridge English</span>
  </footer>
</main>
</body>
</html>
```